Non-Profit Needs Plastic Recycling Infographic

We need a modern infographic to help illustrate international recycling rates for expanded polystyrene plastic. Include the information below and use the attached PowerPoint as an example for your design – the PowerPoint is just to illustrate the information; you do not need to follow it completely.

We have also included our updated color guide.

Please fit the following information into the infographic:
• The one item that is necessary is the global map – the "Global EPS Packaging Recycling" header is not required
• Do NOT include any "chasing arrows" recycling symbols
• the "34 Countries" should read "34 Countries with a Confirmed Recycling Rate"
• "34 Countries" should be an information block along with the "21 Countries"
• The "32 Countries" and "62 Countries" should be included in the graph image – we have given a pie graph as an example, though it can be another graph
• "Leading EPS Recyclate Sources" should have the following four blocks associated with it: Automotive, Seafood & Fishers, Furniture, and Appliances; use attached photos for blocks
• The lorem ipsum vertical information blocks should include 3 columns:
#1: "Developing Countries Recycle EPS" – include country outline of Guatemala; include the text "EPS manufacturing is working with government in Guatemala. Where an EPS molder exists is the easiest way to initiate EPS recycling. Work with the EPS manufacturing sector can promote quick startup of B2B recycling programs."
#2: "Small Islands Recycle EPS" – include country outline of Dominican Republic; include the text "An EPS recycling program in the Dominican Republic highlighted the need for new polystyrene recycling technologies. Through their work with machinery specialists, they were able to identify a solution that then spread to other nations."
#3: "Local Communities Recycle EPS" – include country outline of China; include text "EPS startups can lead to successful recycling collection programs. Lanfeng Neighborhood Office in Xiamen City, China, was already receiving polystyrene for recycling when they were able to procure a densifier. Since installation, the program has spread to five machines located across the city."
• Under the "Unified Resource Stewardship Compact" statement, include the following: "Criteria could be tailored to specific applications, allowing for country-specific flexibility. This approach would also help to develop standards on a material basis and allow countries to focus on scientific research and assess availability of recycling programs."

Font styles to use
Sans Serif

Requirements
Must have
• 1. Global EPS Recycling Map (see attached documents), 2. Infographic should be vertical in design, NOT horizontal
Should not have
• Chasing Arrows Recycling Symbols

```html
<!DOCTYPE html>
<html lang="en">
<head>
<meta charset="utf-8">
<title>International Recycling Rates for Expanded Polystyrene (EPS)</title>
<link href="https://fonts.googleapis.com/css2?family=Poppins:wght@400;500;600;700;800&family=Open+Sans:wght@400;700&display=swap" rel="stylesheet">
<style>
:root{
  --navy:#1a2d4f;
  --orange:#ef8455;
  --yellow:#f2b134;
  --olive:#5e6e0c;
  --cream:#f3efe6;
  --barcream:#f2eee4;
  --charcoal:#4a4a4a;
  --gray:#c4c5c8;
  --white:#ffffff;
  --mapgray:#d9cfcc;
  --blue:#0b4a7a;
}
*{margin:0;padding:0;box-sizing:border-box}
html,body{width:763px;height:1200px;overflow:hidden}
body{background:var(--cream);font-family:'Poppins',sans-serif;position:relative;color:var(--navy)}
.abs{position:absolute}

.header-band{left:0;top:0;width:763px;height:440px;background:var(--navy)}
.title-1{left:0;width:763px;top:18px;text-align:center;color:#f1ede2;font-weight:700;font-size:28.5px;letter-spacing:.2px}
.title-2{left:0;width:763px;top:52px;text-align:center;color:var(--orange);font-weight:700;font-size:37px;letter-spacing:.3px}
.divider{left:0;top:438px;width:763px;height:6px;background:#57534f}

.map-panel{left:0;top:112px;width:527px;height:265px;background:#fdfcf9}
.map-art{left:30px;top:8px;width:440px;height:215px;background:linear-gradient(160deg,#d9cfcc 0%,#c9c0b6 45%,#8a9436 60%,#d9cfcc 100%);border-radius:6px;opacity:.9}
.legend{left:10px;top:240px;width:460px;height:18px;border-bottom:1px solid #444;display:flex;align-items:center;font-family:'Open Sans',sans-serif;font-size:7.5px;color:#333;white-space:nowrap}
.legend .arrow{width:0;height:0;border-left:6px solid #111;border-top:5px solid transparent;border-bottom:5px solid transparent;margin-right:5px;flex:none}
.legend .info{font-weight:700;margin-right:16px}
.legend .sw{display:inline-block;width:12px;height:12px;margin-right:5px;flex:none}
.legend .item{display:inline-flex;align-items:center;margin-right:34px;white-space:nowrap}
.map-caption{left:64px;top:398px;color:#fff;font-weight:700;font-size:10.5px;letter-spacing:-.1px}

.rates-title{left:546px;top:110px;color:#fff;font-weight:600;font-size:9px}
.rate{left:547px;width:184px;height:16px;display:flex;align-items:center;font-weight:700;font-size:14px;line-height:1}
.rate .fill{height:100%;display:flex;align-items:center;padding-left:7px;white-space:nowrap}
.rate .val{position:absolute;right:6px;top:1px;font-weight:500;font-size:14px}
.rate.light{background:var(--barcream)}
.rate.light .fill{color:var(--navy)}
.rate.light .val{color:var(--orange)}
.rate.dark{background:#555}
.rate.dark .fill,.rate.dark .val{color:#fff}

.overview-title{left:35px;top:484px;font-weight:700;font-size:20.5px;color:var(--navy)}
.count-box{left:33px;top:522px;width:338px;height:181px;background:var(--navy)}
.count-box .rule{left:166px;top:18px;width:2px;height:140px;background:var(--yellow)}
.stat{top:14px;width:166px;text-align:center;color:#fff;font-weight:700}
.stat .num{font-size:62px;line-height:1;letter-spacing:-2px;font-weight:800}
.stat .lbl{font-size:25px;line-height:1;margin-top:4px}
.stat .sub{font-size:14.5px;line-height:1.4}
.stat-a{left:3px}.stat-a .num,.stat-a .lbl{color:var(--orange)}
.stat-b{left:168px}.stat-b .num,.stat-b .lbl{color:var(--yellow)}
.count-bar{left:33px;top:712px;width:338px;height:18px;display:flex;font-size:10px;color:#fff}
.count-bar div{display:flex;align-items:center;justify-content:center}

.big62{left:428px;top:500px;font-weight:800;font-size:46px;color:var(--navy);line-height:1}
.big62-label{left:428px;top:544px;font-weight:700;font-size:14px;line-height:1.3;color:var(--navy)}
.big62-label .caps{font-size:14.5px}
.dots{left:427px;top:623px;display:flex;gap:5px}
.dots span{width:5.5px;height:5.5px;border-radius:50%;background:#333}
.big32{left:430px;top:652px;font-weight:800;font-size:38px;color:var(--orange);line-height:1}
.big32-label{left:430px;top:688px;font-weight:700;font-size:13px;color:var(--orange);line-height:1.25}
.pie{left:500px;top:510px}
.pie-label-no{left:537px;top:490px;font-weight:700;font-size:13px;color:var(--orange)}
.pie-label-yes{left:612px;top:716px;font-weight:700;font-size:14px;color:var(--navy)}

.band{left:0;top:810px;width:412px;height:62px;background:var(--gray)}
.col{top:797px;width:100px;height:371px}
.col .strip{height:8px}
.col .strip2{height:6px;background:#555}
.col .body{position:absolute;left:0;top:14px;width:100%;bottom:0}
.col .head{position:absolute;left:0;top:14px;width:100%;height:82px;background:#eeeeef;clip-path:polygon(0 0,100% 0,100% 75%,50% 100%,0 75%)}
.col .head::before{content:"";position:absolute;left:5px;right:5px;top:4px;height:1px;background:#777}
.col h3{position:absolute;left:0;top:30px;width:100%;text-align:center;font-size:9.5px;font-weight:600;line-height:1.2;color:var(--navy)}
.col .outline{position:absolute;left:22px;width:56px;height:54px;top:108px;border-radius:40% 35% 45% 30%}
.col p{position:absolute;left:4px;right:4px;text-align:center;font-size:8.6px;line-height:1.22;font-weight:500}
.col-1{left:15px}.col-1 .strip,.col-1 .body{background:var(--yellow)}
.col-1 .outline{background:#a66b21}.col-1 p{top:182px;color:var(--navy)}
.col-2{left:158px}.col-2 .strip{background:#555}.col-2 .body{background:var(--charcoal)}
.col-2 .outline{background:#2e2e2e;height:44px;top:106px}.col-2 p{top:154px;color:#fff}
.col-3{left:300px;width:97px}.col-3 .strip,.col-3 .body{background:var(--orange)}
.col-3 .outline{background:#c45e35;height:38px;left:20px;top:106px}.col-3 p{top:168px;color:var(--navy)}

.sources{left:416px;top:811px;width:337px;height:147px;background:var(--orange)}
.sources h2{position:absolute;left:0;width:100%;top:10px;text-align:center;font-weight:700;font-size:17.5px;color:var(--navy);white-space:nowrap}
.source{position:absolute;top:44px;width:73px}
.source .photo{width:73px;height:71px;border:3px solid var(--navy)}
.source span{display:block;text-align:center;color:#fff;font-weight:700;font-size:8.3px;line-height:1.2;margin-top:8px}

.compact-title{left:416px;top:982px;width:338px;font-weight:700;font-size:16.4px;line-height:1.2;color:var(--orange);white-space:nowrap}
.compact-text{left:416px;top:1006px;width:338px;font-weight:700;font-size:15.2px;line-height:1.22;text-align:justify;color:var(--navy)}
</style>
</head>
<body>

<div class="abs header-band"></div>
<h1 class="abs title-1">INTERNATIONAL RECYCLING RATES FOR</h1>
<div class="abs title-2">EXPANDED POLYSTYRENE (EPS)</div>

<section class="abs map-panel">
  <div class="abs map-art" role="img" aria-label="World map highlighting regions with EPS post-use recycling above 30% in olive, 10–30% in blue, with orange markers on program locations"></div>
  <div class="abs legend">
    <span class="arrow"></span><span class="info">INFO</span>
    <span class="item"><span class="sw" style="background:var(--olive)"></span><span>Post - Use Recycling&nbsp;<b style="color:var(--olive)">Above 30%</b></span></span>
    <span class="item"><span class="sw" style="background:var(--blue)"></span><span>Post - Use Recycling&nbsp;<b style="color:var(--blue)">10-30%</b></span></span>
    <span class="item"><span class="sw" style="background:var(--mapgray)"></span><span>Information Unavailable</span></span>
  </div>
</section>
<div class="abs map-caption">A WORLD MAP HIGHLIGHTING REGIONS WITH EPS RECYCLING PROGRAMS</div>

<div class="abs rates-title">EPS foam packaging &amp; recycling rate</div>
<div class="abs rate light" style="top:130px"><div class="fill" style="width:131px;background:var(--orange)">North America</div><span class="val">64%</span></div>
<div class="abs rate light" style="top:156px"><div class="fill" style="width:66px;background:var(--yellow)">Brazil</div><span class="val">30.9%</span></div>
<div class="abs rate light" style="top:181px"><div class="fill" style="width:79px;background:var(--olive);color:#fff">Europe</div><span class="val">37%</span></div>
<div class="abs rate light" style="top:206px"><div class="fill" style="width:100px;background:var(--orange)">UK</div><span class="val">50%</span></div>
<div class="abs rate light" style="top:230px"><div class="fill" style="width:138px;background:var(--yellow)">Norway</div><span class="val">76%</span></div>
<div class="abs rate dark" style="top:261px"><div class="fill" style="width:66px;background:var(--orange)">India</div><span class="val">30%</span></div>
<div class="abs rate dark" style="top:287px"><div class="fill" style="width:66px;background:var(--yellow)">China</div><span class="val">%</span></div>
<div class="abs rate dark" style="top:312px"><div class="fill" style="width:79px;background:var(--olive)">Europe</div><span class="val">37%</span></div>
<div class="abs rate dark" style="top:337px"><div class="fill" style="width:100px;background:var(--orange)">UK</div><span class="val">50%</span></div>
<div class="abs rate dark" style="top:361px"><div class="fill" style="width:138px;background:var(--yellow)">Norway</div><span class="val">76%</span></div>

<div class="abs divider"></div>

<h2 class="abs overview-title">Global EPS Recycling Overview</h2>
<section class="abs count-box">
  <div class="abs rule"></div>
  <div class="abs stat stat-a"><div class="num">34</div><div class="lbl">Countries</div><div class="sub">with a Confirmed<br>Recycling&nbsp; Rate</div></div>
  <div class="abs stat stat-b"><div class="num">21</div><div class="lbl">Countries</div><div class="sub">with a Confirmed<br>Recycling&nbsp; Rate<br>above 30%</div></div>
</section>
<div class="abs count-bar"><div style="width:208px;background:var(--navy)">34 Countries</div><div style="width:130px;background:var(--orange)">21 Countries</div></div>

<div class="abs big62">62</div>
<div class="abs big62-label"><span class="caps">COUNTRIES</span><br>Recycle<br>EPS</div>
<div class="abs dots"><span></span><span></span><span></span><span></span><span></span><span></span><span></span><span></span><span></span></div>
<div class="abs big32">32%</div>
<div class="abs big32-label">COUNTRIES<br>Have EPS<br>Recycling</div>

<svg class="abs pie" width="200" height="200" viewBox="0 0 200 200" aria-label="Pie chart: EPS recycling versus no recycling">
  <circle cx="103" cy="101" r="92" fill="none" stroke="#f5e76a" stroke-width="3"/>
  <path d="M103 9 A92 92 0 0 1 167 167" fill="none" stroke="var(--navy)" stroke-width="3"/>
  <path d="M11 101 A92 92 0 0 1 103 9" fill="none" stroke="#e0a22a" stroke-width="4"/>
  <path d="M11 101 A92 92 0 0 0 150 180" fill="none" stroke="#e0a22a" stroke-width="4"/>
  <circle cx="103" cy="101" r="82" fill="#f9cf7f"/>
  <path d="M103 101 L103 19 A82 82 0 0 1 163 157 Z" fill="#2e4670"/>
  <path d="M103 101 L103 26 A75 75 0 0 1 158 152 Z" fill="var(--navy)"/>
  <path d="M103 101 L158 152 A75 75 0 1 1 103 26 Z" fill="var(--yellow)"/>
  <circle cx="103" cy="101" r="86" fill="none" stroke="#fff" stroke-width="1.5" stroke-dasharray="300 40"/>
  <polyline points="163,5 165,5 165,73" fill="none" stroke="var(--orange)" stroke-width="1.2"/>
  <circle cx="165" cy="73" r="5" fill="var(--orange)"/>
  <polyline points="64,136 64,214" fill="none" stroke="var(--navy)" stroke-width="1.2"/>
  <circle cx="64" cy="136" r="5" fill="var(--navy)"/>
</svg>
<div class="abs pie-label-no">No Recycling</div>
<svg class="abs" style="left:563px;top:722px" width="50" height="4"><line x1="0" y1="2" x2="48" y2="2" stroke="var(--navy)" stroke-width="1.2"/></svg>
<div class="abs pie-label-yes">EPS Recycling</div>

<div class="abs band"></div>
<article class="abs col col-1">
  <div class="strip"></div><div class="strip2"></div>
  <div class="body"></div><div class="head"></div>
  <h3>Developing<br>Countries<br>Recycle<br>EPS</h3>
  <div class="outline" role="img" aria-label="Country outline of Guatemala"></div>
  <p>EPS manufacturing is working with government in Guatemala. Where an EPS molder exists is the easiest way to initiate EPS recycling. Work with the EPS manufacturing sector can promote quick startup of B2B recycling programs</p>
</article>
<article class="abs col col-2">
  <div class="strip"></div><div class="strip2"></div>
  <div class="body"></div><div class="head"></div>
  <h3>Local<br>Communities<br>Recycle EPS</h3>
  <div class="outline" role="img" aria-label="Country outline of China"></div>
  <p>EPS startups can lead to successful recycling collection programs. Lanfeng Neighborhood Office in Xiamen City, China, was already receiving polystyrene for recycling when they were able to procure a densifier. Since installation, the program has spread to five machines located across the city</p>
</article>
<article class="abs col col-3">
  <div class="strip"></div><div class="strip2"></div>
  <div class="body"></div><div class="head"></div>
  <h3>Small Islands<br>Recycle EPS</h3>
  <div class="outline" role="img" aria-label="Country outline of the Dominican Republic"></div>
  <p>An EPS recycling program in the Dominican Republic highlighted the need for new polystyrene recycling technologies. Through their work with machinery specialists, they were able to identify a solution that then spread to other nations</p>
</article>

<section class="abs sources">
  <h2>LEADING EPS RECYCLATE SOURCES</h2>
  <div class="source" style="left:15px"><div class="photo" role="img" aria-label="Photo of a worker carrying a large white EPS block" style="background:linear-gradient(135deg,#8ea3b8,#e9ecef 60%,#6a7d8e)"></div><span>FURNITURE</span></div>
  <div class="source" style="left:93px"><div class="photo" role="img" aria-label="Photo of fish packed in a white EPS box" style="background:linear-gradient(160deg,#c7ccd2,#f4f5f6 55%,#dfe2e6)"></div><span>SEAFOOD &amp;<br>FISHERS</span></div>
  <div class="source" style="left:173px"><div class="photo" role="img" aria-label="Photo of a truck bumper cross-section showing foam core" style="background:linear-gradient(170deg,#8f9690,#d6d3dc 55%,#f3f3f3)"></div><span>AUTOMOTIVE</span></div>
  <div class="source" style="left:255px"><div class="photo" role="img" aria-label="Photo of a washing machine appliance" style="background:linear-gradient(160deg,#e2e3e4,#b9bcbf 60%,#efefef)"></div><span>APPLIANCES</span></div>
</section>

<div class="abs compact-title">*Unified Resource Stewardship Compact</div>
<p class="abs compact-text">Criteria could be tailored to specific applications, allowing for country-specific flexibility. This approach would also help to develop standards on a material basis and allow countries to focus on scientific research and assess availability of recycling programs.</p>

</body>
</html>
```